Business card design needed for Automotive Reconditioning business

I have a logo design i just cant decide on the best color or layout for the business card, I will upload all the files so you can see all colors schemes we are considering. I have other file formats if needed let me know.

Target Market(s)

automotive dealerships

Contact Information for Business Card

HERE are the Descriptions and info needed on the card:
Interior Repair: Leather carpet burns panels dash Deoderize
Dealer products and Vin Verify
( spot for name and cell number) My name is Norman Bexley phone 614 352-4180 Title COO www.QuorvalMotive.com

Font styles to use
Sans Serif
Other font styles liked:
• what ever you think looks best

Requirements
Must have
• Must be able to change the name and phone for employees

```html
<!DOCTYPE html>
<html lang="en">
<head>
<meta charset="utf-8">
<title>Quorval Motive Reconditioning Corp. – Business Card</title>
<link rel="stylesheet" href="https://fonts.googleapis.com/css2?family=Roboto:wght@300;400;700&display=swap">
<style>
  :root {
    --backdrop: #5a5a5c;
    --ink: #1c1c1c;
    --lime: #8fbf3d;
    --white: #ffffff;
    --muted: #3a3a3a;
    --silver: #e6e6e6;
  }
  * { margin: 0; padding: 0; box-sizing: border-box; }
  html, body {
    width: 1073px; height: 1200px; overflow: hidden;
    background: var(--backdrop);
    font-family: "Roboto", Arial, sans-serif;
  }
  .card {
    position: absolute; left: 115px;
    width: 843px; height: 481px;
    overflow: hidden;
  }
  .card-front { top: 104px; background: var(--ink); }
  .card-back { top: 617px; background: var(--lime); }
  .card-shape { position: absolute; inset: 0; width: 100%; height: 100%; }

  .brand {
    position: absolute;
    display: flex; align-items: center; gap: 12px;
    color: var(--silver); font-weight: 700;
    text-transform: uppercase; line-height: 1.1;
  }
  .brand-mark { background: var(--lime); flex: none; }
  .brand-front { left: 141px; top: 240px; font-size: 46px; letter-spacing: 1px; }
  .brand-front .brand-mark { width: 22px; height: 22px; }
  .brand-front small { display: block; font-size: 19px; letter-spacing: 0.5px; margin-top: 6px; }
  .brand-back { left: 574px; top: 72px; font-size: 25px; }
  .brand-back .brand-mark { width: 12px; height: 12px; }
  .brand-back small { display: block; font-size: 10.5px; margin-top: 3px; }

  .person-name {
    position: absolute; left: 77px; top: 78px;
    font-size: 29px; font-weight: 700; letter-spacing: 3px;
    color: var(--ink); text-transform: uppercase;
  }
  .name-rule {
    position: absolute; left: 77px; top: 122px;
    width: 115px; height: 2px; background: var(--ink);
  }
  .person-title {
    position: absolute; left: 77px; top: 137px;
    font-size: 21px; font-weight: 300; letter-spacing: 1px; color: var(--muted);
  }
  .contact {
    position: absolute; left: 77px;
    display: flex; align-items: center;
    font-size: 21px; letter-spacing: 3px; color: var(--white);
  }
  .contact svg { width: 20px; height: 20px; margin-right: 31px; fill: var(--white); }
  .contact-phone { top: 230px; }
  .contact-web { top: 272px; }
  .services {
    position: absolute; left: 80px; width: 638px; top: 364px;
    text-align: center; font-size: 22px; line-height: 28px; color: var(--white);
  }
  .services-rule {
    position: absolute; left: 127px; top: 436px;
    width: 547px; height: 2px; background: var(--white);
  }
</style>
</head>
<body>
  <section class="card card-front">
    <svg class="card-shape" viewBox="0 0 1050 600" preserveAspectRatio="none" aria-hidden="true">
      <path d="M36,0 C520,8 900,240 1050,600 L1050,0 Z" fill="var(--lime)"/>
    </svg>
    <div class="brand brand-front">
      <span class="brand-mark"></span>
      <div>Quorval Motive<small>Reconditioning Corp.</small></div>
    </div>
  </section>

  <section class="card card-back">
    <svg class="card-shape" viewBox="0 0 1050 600" preserveAspectRatio="none" aria-hidden="true">
      <path d="M60,0 C520,8 900,240 1050,600 L1050,0 Z" fill="var(--ink)"/>
    </svg>
    <div class="brand brand-back">
      <span class="brand-mark"></span>
      <div>Quorval Motive<small>Reconditioning Corp.</small></div>
    </div>

    <h1 class="person-name">Norman Bexley</h1>
    <div class="name-rule"></div>
    <p class="person-title">COO</p>

    <p class="contact contact-phone">
      <svg viewBox="0 0 24 24" aria-hidden="true"><path d="M6.6 2.5l3 4.2-1.9 2.1c.9 2.4 2.8 4.8 5.3 6.3l2-1.8 4.3 2.9-1.7 3.8c-6.7-.4-13.4-7.6-13-14.6z"/></svg>
      614 352-4180
    </p>
    <p class="contact contact-web">
      <svg viewBox="0 0 24 24" aria-hidden="true"><path fill="none" stroke="#fff" stroke-width="1.8" d="M12 2a10 10 0 1 0 0 20a10 10 0 1 0 0-20zM2 12h20M12 2c3 3 3 17 0 20M12 2c-3 3-3 17 0 20M4 7h16M4 17h16"/></svg>
      www.quorvalmotive.com
    </p>

    <p class="services">Interior Repair: Leather carpet burns panels dash<br>Deoderize Dealer products and Vin Verify</p>
    <div class="services-rule"></div>
  </section>
</body>
</html>
```